Hall of Fame annnouncement graphic for social media

I need a social media Hall of Fame announcement designed in the styles of some of the examples I've posted. I have attached the two gentlemens head shots ... the names are Dale Prusky and Ted Marrish

It is for the BRANDMOOR LINKS HALL OF FAME also include 2026 Inductees ... I have also attached the logo... make the post in similar colors as the logo.

I need this tomorrow so I am going to pick a winner in the next 24 hours.

```html
<!DOCTYPE html>
<html lang="en">
<head>
<meta charset="utf-8">
<title>Brandmoor Links Hall of Fame – 2026 Inductees</title>
<link rel="stylesheet" href="https://fonts.googleapis.com/css2?family=Cinzel:wght@700;800&family=Playfair+Display:ital@1&family=Poppins:wght@700&display=swap">
<style>
  :root {
    --navy: #0c3079;
    --red: #b3171b;
    --white: #ffffff;
    --paper: #f2f2f2;
    --silver-top: #ffffff;
    --silver-bottom: #b9bcc2;
    --photo-sky: #ededed;
    --photo-grey: #a9a9a9;
    --photo-skin: #d99a80;
    --photo-skin-light: #e9b9a2;
    --photo-shirt: #fbf7f6;
  }
  * { box-sizing: border-box; margin: 0; padding: 0; }
  html, body { width: 1200px; height: 719px; overflow: hidden; background: var(--paper); }
  .post { position: relative; width: 1200px; height: 719px; overflow: hidden; font-family: "Cinzel", serif; }
  .backdrop {
    position: absolute; inset: 0;
    background: linear-gradient(180deg, #f4f4f4 0%, #e3e3e3 40%, #ededed 75%, #dcdcdc 100%);
  }
  .band { position: absolute; left: 0; right: 0; top: 196px; height: 360px; background: var(--navy); }

  .brand {
    position: absolute; left: 58px; top: 62px; width: 366px;
    display: flex; align-items: center; justify-content: center; gap: 14px;
    color: var(--red); font-weight: 700; font-size: 27px; line-height: 32px;
    text-align: center;
    border-bottom: 2px solid var(--red); padding-bottom: 10px;
  }
  .brand-dot { width: 14px; height: 14px; border-radius: 50%; background: var(--red); flex: none; }

  .title { position: absolute; left: 40px; width: 396px; top: 221px; text-align: center; }
  .title-kicker { color: var(--white); font-weight: 700; font-size: 30px; letter-spacing: 2px; line-height: 36px; }
  .title-word {
    font-weight: 800; font-size: 124px; line-height: 106px; letter-spacing: 2px;
    background: linear-gradient(180deg, var(--silver-top) 30%, var(--silver-bottom) 100%);
    -webkit-background-clip: text; background-clip: text; color: transparent;
  }
  .title-of { display: flex; align-items: center; justify-content: center; gap: 18px; height: 48px; }
  .title-of span.rule { width: 130px; height: 2px; background: var(--white); }
  .title-of em { font-family: "Playfair Display", serif; color: var(--white); font-size: 34px; line-height: 1; }

  .inductees-label {
    position: absolute; left: 52px; width: 380px; top: 575px; text-align: center;
    font-weight: 700; font-size: 38px; line-height: 50px; color: var(--navy); white-space: nowrap;
  }
  .inductees-label .year { color: var(--red); }

  .portrait {
    position: absolute; top: 57px; width: 327px; height: 538px;
    border: 3px solid var(--white); overflow: hidden;
  }
  .portrait--one { left: 478px; }
  .portrait--two { left: 832px; border-top-right-radius: 26px; }
  .portrait-photo {
    width: 100%; height: 100%;
    background: linear-gradient(180deg,
      var(--photo-sky) 0%,
      var(--photo-grey) 16%,
      var(--photo-skin) 30%,
      var(--photo-skin-light) 44%,
      var(--photo-shirt) 58%,
      var(--white) 100%);
  }

  .name-tag {
    position: absolute; top: 561px; height: 62px;
    background: var(--red); color: var(--white);
    font-family: "Poppins", sans-serif; font-weight: 700; font-size: 28px;
    display: flex; align-items: center; justify-content: center; white-space: nowrap;
    border: 3px solid var(--white);
    border-radius: 22px 6px 6px 22px;
  }
  .name-tag--one { left: 500px; width: 283px; }
  .name-tag--two { left: 853px; width: 284px; }
</style>
</head>
<body>
  <main class="post">
    <div class="backdrop" role="img" aria-label="Faded black-and-white golf course scene with trees"></div>
    <div class="band"></div>

    <div class="brand"><span class="brand-dot"></span>Brandmoor Links<br>Hall of Fame</div>

    <h1 class="title">
      <div class="title-kicker">BRANDMOOR LINKS</div>
      <div class="title-word">HALL</div>
      <div class="title-of"><span class="rule"></span><em>of</em><span class="rule"></span></div>
      <div class="title-word">FAME</div>
    </h1>

    <p class="inductees-label"><span class="year">2026</span> INDUCTEES</p>

    <figure class="portrait portrait--one">
      <div class="portrait-photo" role="img" aria-label="Head-and-shoulders portrait of inductee Ted Marrish in a white polo shirt"></div>
    </figure>
    <figure class="portrait portrait--two">
      <div class="portrait-photo" role="img" aria-label="Head-and-shoulders portrait of inductee Dale Prusky in a white polo shirt"></div>
    </figure>

    <div class="name-tag name-tag--one">TED MARRISH</div>
    <div class="name-tag name-tag--two">DALE PRUSKY</div>
  </main>
</body>
</html>
```